New Body Mist 250 ml exclusive

We are excited to embark on a new project to design the packaging for body mist:
Amber Drizzle

We are looking for a design that is truly unique and stands out, with a touch of individuality that sets it apart. The design should be eye-catching and visually appealing, drawing attention even from a distance. We want the body mists to have a fun and attractive look that appeals to customers.

To help bring your design to life, we will provide the dimensions of the bottle, which has a capacity of 250ml. The bottle measures 13.3 cm in height and 4.9 cm in diameter (excluding the pump). Additionally, we will also provide the dimensions of the label, which measures 15.1 cm in height and 12.8 cm in width.

We believe that giving you the freedom to put your own unique touch and color choices will help create a truly standout design. We look forward to seeing your creative vision for our body mist.

We shared with you the logo of the body mist and some examples of models that we liked.

Please be informed that the project only includes one design and the remaining three will be completed and paid for through a 1on1 project with the winner of the contest.

Target Market(s)

Supermarket and perfumery stores

Industry/Entity Type

Cosmetics

Font styles to use
Serif

Requirements
Must have
• Uniqueness and attractiveness

```html
<!DOCTYPE html>
<html lang="en">
<head>
<meta charset="utf-8">
<title>Amber Drizzle Body Mist Label</title>
<link href="https://fonts.googleapis.com/css2?family=Allura&family=Playfair+Display:wght@400;500&display=swap" rel="stylesheet">
<style>
  :root {
    --backdrop: #e9eaec;
    --label: #fbfbfc;
    --ink: #141414;
    --gold-deep: #e2ac12;
    --gold-light: #f5e37c;
    --petal-light: #f7c3d3;
    --petal-mid: #ef8aac;
    --petal-deep: #d9589a;
    --tag-pink: #f2a2aa;
    --tag-text: #ffffff;
  }
  html, body {
    margin: 0;
    width: 1200px;
    height: 1200px;
    overflow: hidden;
    background: var(--backdrop);
  }
  .canvas {
    position: relative;
    width: 1200px;
    height: 1200px;
  }
  .label {
    position: absolute;
    left: 300px;
    top: 100px;
    width: 600px;
    height: 1000px;
    background: var(--label);
    box-shadow: 0 6px 24px rgba(0,0,0,0.08);
  }
  .label svg { display: block; }
  .brand-name {
    font-family: "Playfair Display", serif;
    font-weight: 400;
    font-size: 50px;
    letter-spacing: 6px;
    fill: var(--ink);
  }
  .band-title {
    font-family: "Allura", cursive;
    font-size: 130px;
    fill: var(--ink);
  }
  .band-tagline {
    font-family: "Allura", cursive;
    font-size: 36px;
    fill: var(--ink);
  }
  .product-type {
    font-family: "Playfair Display", serif;
    font-weight: 500;
    font-size: 34px;
    letter-spacing: 22px;
    fill: var(--ink);
  }
  .volume {
    font-family: "Playfair Display", serif;
    font-weight: 400;
    font-size: 38px;
    fill: var(--tag-text);
  }
</style>
</head>
<body>
<div class="canvas">
  <div class="label">
    <svg width="600" height="1000" viewBox="0 0 600 1000" xmlns="http://www.w3.org/2000/svg">
      <defs>
        <radialGradient id="petalGlow" cx="50%" cy="50%" r="50%">
          <stop offset="0%" stop-color="var(--petal-deep)"/>
          <stop offset="45%" stop-color="var(--petal-mid)"/>
          <stop offset="85%" stop-color="var(--petal-light)"/>
          <stop offset="100%" stop-color="var(--petal-light)" stop-opacity="0"/>
        </radialGradient>
        <linearGradient id="goldSheen" x1="0" y1="0" x2="1" y2="1">
          <stop offset="0%" stop-color="var(--gold-deep)"/>
          <stop offset="55%" stop-color="var(--gold-light)"/>
          <stop offset="100%" stop-color="var(--gold-deep)"/>
        </linearGradient>
        <linearGradient id="goldStrip" x1="0" y1="0" x2="1" y2="0">
          <stop offset="0%" stop-color="var(--gold-deep)"/>
          <stop offset="50%" stop-color="var(--gold-light)"/>
          <stop offset="100%" stop-color="var(--gold-deep)"/>
        </linearGradient>
        <clipPath id="artClip"><rect width="600" height="800"/></clipPath>
      </defs>

      <text class="brand-name" x="300" y="88" text-anchor="middle">AMBER DRIZZLE</text>

      <g clip-path="url(#artClip)">
        <g role="img" aria-label="Watercolour pink flower illustration, upper left">
          <circle class="flower-area" cx="190" cy="330" r="220" fill="url(#petalGlow)"/>
        </g>
        <g role="img" aria-label="Watercolour pink flower illustration, lower right">
          <circle class="flower-area" cx="440" cy="630" r="210" fill="url(#petalGlow)"/>
        </g>

        <polygon class="diagonal-band" points="0,580 600,240 600,440 0,780" fill="url(#goldSheen)"/>
      </g>

      <g transform="translate(300 510) rotate(-29.5)">
        <text class="band-title" x="0" y="10" text-anchor="middle">Exclusive</text>
        <text class="band-tagline" x="10" y="58" text-anchor="middle">Text here Text here Text here</text>
      </g>

      <rect class="product-strip" x="0" y="800" width="600" height="76" fill="url(#goldStrip)"/>
      <text class="product-type" x="311" y="850" text-anchor="middle">BODY MIST</text>

      <polygon class="volume-tag" points="210,896 390,896 390,964 300,986 210,964" fill="var(--tag-pink)"/>
      <text class="volume" x="300" y="944" text-anchor="middle">250ml</text>
    </svg>
  </div>
</div>
</body>
</html>
```